Professional, elegant brochure for funeral home

We have a funeral home. We would like a 2 sided brochure. On one side will be 3 columns for our cremation options and on the other side would be 2-3 columns of our burial options. Would like to print it and also will be putting it on our website at www.Varnelhaven.com

Use as examples

https://www.brimtolgrace.com/pricing-and-resources/online-cremation-package-options

https://pelladinechapel.com/wp-content/uploads/Cremation-with-Ceremony-Plans.pdf

We only need a simple 1page (front and back brochure). Once we have decided on the designer I can provide the final content to be placed on the brochure.

Target Market(s)

We are family owned business so Something soft, inviting, personable and looks professionally done.

Industry/Entity Type

Funeral Home

Requirements
Must have
• Look professional. Easy to read
Nice to have
• Softer Muted comforting colors. No bright colors.

```html
<!DOCTYPE html>
<html lang="en">
<head>
<meta charset="utf-8">
<title>Varnel Haven Funeral Home – Brochure</title>
<link rel="stylesheet" href="https://fonts.googleapis.com/css2?family=Montserrat:wght@500;600;700&family=Oswald:wght@500;600&family=Open+Sans:wght@400;600&display=swap">
<style>
:root{
  --blue:#1670b3;
  --blue-dark:#0d5a94;
  --green:#a9cc3c;
  --card:#eeeff1;
  --text:#4b4f55;
  --bg:#e6e6e6;
  --white:#ffffff;
}
*{box-sizing:border-box;margin:0;padding:0}
html,body{width:1200px;height:2301px;overflow:hidden}
body{background:var(--bg);font-family:"Open Sans",Arial,sans-serif;color:var(--text);position:relative}
.page{position:absolute;left:205px;width:790px;height:1110px;background:var(--white);overflow:hidden;box-shadow:0 2px 8px rgba(0,0,0,.12)}
.page--front{top:30px}
.page--back{top:1162px}

.hero-art{position:absolute;left:0;top:0;width:790px;height:560px}
.brand{position:absolute;left:36px;top:34px;font-family:"Montserrat",sans-serif;font-weight:600;font-size:17px;letter-spacing:2px;color:var(--white);display:flex;align-items:center;gap:8px}
.brand__dot{width:10px;height:10px;border-radius:50%;background:var(--white)}
.plan-title{position:absolute;left:34px;top:78px;font-family:"Oswald",sans-serif;font-weight:600;color:var(--white);font-size:88px;line-height:78px;letter-spacing:-1px}
.plan-rule{position:absolute;left:36px;top:258px;width:70px;height:5px;background:var(--blue)}
.plan-rule::after{content:"";position:absolute;left:70px;top:2px;width:250px;height:1px;background:rgba(255,255,255,.8)}
.plan-tagline{position:absolute;left:36px;top:268px;font-family:"Montserrat",sans-serif;font-weight:600;font-size:14px;line-height:16px;color:var(--white)}

.section-title{position:absolute;left:36px;font-family:"Montserrat",sans-serif;font-weight:700;color:var(--blue);font-size:29px}
.front-title{top:566px;padding-bottom:4px;border-bottom:3px solid var(--green)}
.front-sub{position:absolute;left:36px;top:618px;font-family:"Montserrat",sans-serif;font-weight:500;font-size:16px;color:var(--blue)}

.plans{position:absolute;left:37px;top:668px;display:flex;gap:15px}
.plan-card{position:relative;width:230px;height:298px;background:var(--card);padding:70px 20px 0 22px}
.plan-card__tab{position:absolute;left:24px;top:-12px;width:182px;height:44px;background:var(--blue);color:var(--white);font-family:"Montserrat",sans-serif;font-weight:600;font-size:17px;display:flex;align-items:center;justify-content:center;border-radius:0 0 6px 6px}
.plan-card__tab::before,.plan-card__tab::after{content:"";position:absolute;top:0;border-bottom:12px solid var(--blue-dark)}
.plan-card__tab::before{left:-12px;border-left:12px solid transparent}
.plan-card__tab::after{right:-12px;border-right:12px solid transparent}
.plan-list{list-style:none}
.plan-list li{position:relative;padding-left:22px;font-family:"Montserrat",sans-serif;font-weight:600;font-size:11.5px;line-height:13px;color:#3d4148;margin-bottom:10px}
.plan-list li::before,.section-list h3::before{content:"";position:absolute;left:0;top:1px;width:9px;height:9px;border-top:3px solid var(--blue);border-right:3px solid var(--blue);transform:rotate(45deg) scale(.8);transform-origin:center}
.plan-card__price{position:absolute;left:46px;bottom:16px;font-family:"Montserrat",sans-serif;font-weight:600;font-size:15px;color:var(--blue)}

.importance{position:absolute;left:38px;top:996px;width:720px}
.importance h2{font-family:"Montserrat",sans-serif;font-weight:700;font-size:17px;color:var(--blue);margin-bottom:4px}
.importance p{font-size:12px;line-height:13px;color:var(--blue)}

.footer-band{position:absolute;left:0;bottom:0;width:790px;height:32px}
.footer-band__url{position:absolute;left:0;right:0;bottom:8px;text-align:center;font-family:"Montserrat",sans-serif;font-weight:600;font-size:12px;color:var(--white)}

.burial-photo{position:absolute;left:0;top:0;width:790px;height:330px;background:linear-gradient(160deg,#c9c83a 0%,#8aa63a 40%,#6a8a30 70%,#b5b342 100%)}
.burial-bar{position:absolute;left:0;top:330px;width:790px;height:12px;background:var(--blue)}
.back-title{top:360px;font-size:38px}
.back-sub{position:absolute;left:38px;top:413px;width:460px;font-size:13px;line-height:15px;color:var(--text)}
.section-list{position:absolute;left:38px;top:462px;width:718px}
.section-list h3{position:relative;padding-left:22px;font-family:"Montserrat",sans-serif;font-weight:600;font-size:15px;color:var(--blue);margin-bottom:5px}
.section-list h3.small{font-size:13px}
.section-list p{padding-left:22px;font-size:10.5px;line-height:12.5px;color:var(--text);text-align:justify;margin-bottom:8px}
.section-list p.lead{margin-bottom:7px}
.section-list .block{margin-bottom:16px}
.contact-pill{position:absolute;left:36px;top:946px;background:var(--green);color:var(--white);font-family:"Montserrat",sans-serif;font-weight:600;font-size:12.5px;padding:5px 14px;border-radius:14px}
.locations{position:absolute;left:60px;top:990px;display:flex;gap:100px}
.location h4{font-family:"Montserrat",sans-serif;font-weight:700;font-size:12px;color:var(--blue);margin-bottom:4px}
.location p{font-size:10.5px;line-height:19px;color:var(--blue);display:flex;align-items:center;gap:8px}
.location svg{width:11px;height:11px}
</style>
</head>
<body>

<section class="page page--front">
  <svg class="hero-art" viewBox="0 0 790 560" aria-hidden="false">
    <defs>
      <linearGradient id="heroTone" x1="0" y1="0" x2="1" y2="1">
        <stop offset="0" stop-color="#a7cf3a"/>
        <stop offset=".45" stop-color="#8fa84a"/>
        <stop offset="1" stop-color="#c7b79b"/>
      </linearGradient>
    </defs>
    <path role="img" aria-label="Photograph of an older couple resting together on a park bench among green trees" d="M0 0H790V400C640 520 420 555 260 528C150 510 60 440 0 330Z" fill="url(#heroTone)"/>
    <path d="M0 300C40 470 200 560 400 560C560 560 700 510 790 440V400C640 520 420 555 260 528C150 510 60 440 0 330Z" fill="#1670b3"/>
    <path d="M130 498L138 440L190 514Z" fill="#1670b3"/>
  </svg>

  <div class="brand"><span class="brand__dot"></span>VARNEL HAVEN</div>
  <h1 class="plan-title">LIVE<br>WELL PLAN</h1>
  <div class="plan-rule"></div>
  <p class="plan-tagline">Planning Aheade can make all the difference<br>to your family</p>

  <h2 class="section-title front-title">Cremation with Ceremony Plans</h2>
  <p class="front-sub">Prices current as of February 1, 2020</p>

  <div class="plans">
    <article class="plan-card">
      <div class="plan-card__tab">Focus On Life</div>
      <ul class="plan-list">
        <li>Professional Services</li>
        <li>Transfer of Deceased</li>
        <li>Care &amp; Preparation</li>
        <li>Funeral Ceremony</li>
        <li>Hearse</li>
        <li>Utility Vehicle</li>
        <li>Cremation performed<br>at our On-Site<br>Crematory</li>
      </ul>
      <p class="plan-card__price">Plan Price: $6,160</p>
    </article>
    <article class="plan-card">
      <div class="plan-card__tab">Funerals</div>
      <ul class="plan-list">
        <li>Professional Services</li>
        <li>Transfer of Deceased</li>
        <li>Care &amp; Preparation</li>
        <li>Funeral Ceremony at<br>Pelladine Chapel</li>
        <li>Utility Vehicle</li>
        <li>Cremation performed<br>at our On-Site<br>Crematory</li>
      </ul>
      <p class="plan-card__price">Plan Price: $5,685</p>
    </article>
    <article class="plan-card">
      <div class="plan-card__tab">Cremation</div>
      <ul class="plan-list">
        <li>Professional Services</li>
        <li>Transfer of Deceased</li>
        <li>Care &amp; Preparation</li>
        <li>Visitation (2 hours)</li>
        <li>Utility Vehicle</li>
        <li>Cremation performed<br>at our On-Site<br>Crematory</li>
      </ul>
      <p class="plan-card__price">Plan Price: $5,410</p>
    </article>
  </div>

  <div class="importance">
    <h2>The Importance of Ceremony</h2>
    <p>Meaningful ceremonies and rituals create a transformative life experience. Reflecting and remembering a person's legacy in the presence of gathered community...this is when healing begins.</p>
  </div>

  <svg class="footer-band" viewBox="0 0 790 32" preserveAspectRatio="none" aria-hidden="true">
    <rect width="790" height="32" fill="#0d5a94"/>
    <path d="M0 0H180L200 32H0Z" fill="#a9cc3c"/>
  </svg>
  <p class="footer-band__url">www.varnelhaven.com</p>
</section>

<section class="page page--back">
  <div class="burial-photo" role="img" aria-label="Photograph of a couple walking hand in hand through a sunlit autumn park"></div>
  <div class="brand"><span class="brand__dot"></span>VARNEL HAVEN</div>
  <div class="burial-bar"></div>

  <h2 class="section-title back-title">All About Burials</h2>
  <p class="back-sub">Traditional. Profound. Healing. Design a permanent resting place for your loved one.</p>

  <div class="section-list">
    <div class="block">
      <h3>Graveside Funeral Services</h3>
      <p class="lead">Express the life of your loved one and create a place for family and friends to gather.</p>
      <p>We can help you design a meaningful and healing service to take place at the graveside. These services can take place outdoors or even inside a mausoleum. We'll guide you through the process of personalizing both the service and the site in multiple ways. Working with your Funeral Director, you can select readings, speakers and create spiritual moments. You can include military honors, masonic rites and religious leadership. When it comes to memorialization, we offer many options. Your selection may include a flat memorial, upright monument, ledger, mausoleum plate, memorial benches or private estates. We're here to share our expertise, with professionalism and compassion. Contact us with any questions you may have.</p>
    </div>
    <div class="block">
      <h3>Committal Services</h3>
      <p class="lead">A graveside service takes place after a funeral and can be a profound healing experience.</p>
      <p>Funerals often take place at the mortuary chapel or at your place of religious worship. In that case, an internment and committal service can follow at the graveside. These are important gatherings to commemorate a life and mark the end of physical closeness. Family and friends gather to commit a loved one to the earth and say final farewells together. A committal service is symbolic and a helpful step in healing.</p>
    </div>
    <div class="block">
      <h3 class="small">Immediate Burials</h3>
      <p class="lead">Together with your funeral professional, we can guide you through all of the arrangements.</p>
      <p>Burials are often an unexpected need, and we can handle every detail should this option make sense for you and your family. Please call us any time to discuss your needs. Our mission is to ease your burden.</p>
    </div>
    <div class="block">
      <h3 class="small">It's All about the Relationship</h3>
      <p class="lead">Together with your funeral professional, we can guide you through all of the arrangements.</p>
      <p>Honoring the life of your loved one means you value the relationship you shared. We look forward to helping you decide how to celebrate that bond, and honor the unique individual you've lost. We can make suggestions to enhance your tribute ideas. Together we will create a fitting and memorable event. Contact us today to discuss the possibilities.</p>
    </div>
  </div>

  <p class="contact-pill">Contact Us to Arrange for Cremation Services</p>

  <div class="locations">
    <div class="location">
      <h4>Varnel Haven Funeral Home - Brookfield</h4>
      <p>1840 Alder Road Brookfield, NY 14300</p>
      <p><svg viewBox="0 0 12 12" aria-hidden="true"><path d="M1 3C1 1.5 4 1 6 1S11 1.5 11 3V4H8.5V3H3.5V4H1ZM2.5 5H9.5L10.5 11H1.5Z" fill="#a9cc3c"/></svg>(555) 201-4410</p>
      <p><svg viewBox="0 0 12 12" aria-hidden="true"><circle cx="6" cy="6" r="5" fill="none" stroke="#a9cc3c" stroke-width="1.4"/><path d="M1 6H11M6 1C3.5 4 3.5 8 6 11M6 1C8.5 4 8.5 8 6 11" fill="none" stroke="#a9cc3c" stroke-width="1"/></svg>www.varnelhaven.com</p>
    </div>
    <div class="location">
      <h4>Varnel Haven Funeral Home - Easton</h4>
      <p>3125 Linden Avenue Easton, NY 14390</p>
      <p><svg viewBox="0 0 12 12" aria-hidden="true"><path d="M1 3C1 1.5 4 1 6 1S11 1.5 11 3V4H8.5V3H3.5V4H1ZM2.5 5H9.5L10.5 11H1.5Z" fill="#a9cc3c"/></svg>(555) 201-7732</p>
      <p><svg viewBox="0 0 12 12" aria-hidden="true"><circle cx="6" cy="6" r="5" fill="none" stroke="#a9cc3c" stroke-width="1.4"/><path d="M1 6H11M6 1C3.5 4 3.5 8 6 11M6 1C8.5 4 8.5 8 6 11" fill="none" stroke="#a9cc3c" stroke-width="1"/></svg>www.varnelhaven.com</p>
    </div>
  </div>

  <svg class="footer-band" viewBox="0 0 790 32" preserveAspectRatio="none" aria-hidden="true">
    <rect width="790" height="32" fill="#0d5a94"/>
    <path d="M0 0H180L200 32H0Z" fill="#a9cc3c"/>
  </svg>
</section>

</body>
</html>
```